Lantern Hearthworks Business Cards

Looking to create simple business cards that highlight our unique three sided triangle fire pit design with the colors and font of our logo, listed below.

Colors

Designer to choose colors to be used in the design.

Requirements
Must have
• Looking for something simple that includes a picture of our fire pit with name, website (lanternhearthworks.com), phone number and email. Want to keep the color mostly orange and black.
• Font is gotham(medium) and orange color code is #ee6e22

```html
<!DOCTYPE html>
<html lang="en">
<head>
<meta charset="utf-8">
<title>Lantern Hearthworks Business Cards</title>
<link rel="stylesheet" href="https://fonts.googleapis.com/css2?family=Montserrat:wght@400;500;600&display=swap">
<style>
  :root {
    --orange: #ee6e22;
    --charcoal: #1d1d1d;
    --graphite: #595959;
    --paper: #f5f5f5;
    --backdrop: #9a9a9a;
    --white: #ffffff;
  }
  * { margin: 0; padding: 0; box-sizing: border-box; }
  html, body { width: 1200px; height: 1048px; overflow: hidden; }
  body {
    background: var(--backdrop);
    font-family: "Montserrat", Arial, sans-serif;
    position: relative;
  }
  .card {
    position: absolute;
    left: 288px;
    width: 624px;
    height: 357px;
    overflow: hidden;
    box-shadow: 1px 2px 4px rgba(0,0,0,0.35);
  }
  .card--front { top: 144px; background: var(--paper); }
  .card--back {
    top: 547px;
    background: var(--charcoal);
    display: flex;
    align-items: center;
    justify-content: center;
  }

  .product-photo {
    position: absolute;
    left: 0; top: 0;
    width: 271px; height: 357px;
    background:
      radial-gradient(ellipse 70px 55px at 160px 160px, rgba(238,110,34,0.85), rgba(238,110,34,0) 100%),
      linear-gradient(160deg, #2c2c2c, #141414);
  }
  .accent-bar {
    position: absolute;
    left: 271px; top: 0;
    width: 6px; height: 357px;
    background: var(--orange);
  }
  .accent-notch {
    position: absolute;
    left: 277px; top: 198px;
    width: 0; height: 0;
    border-top: 18px solid transparent;
    border-bottom: 18px solid transparent;
    border-left: 14px solid var(--orange);
  }
  .brand-name {
    position: absolute;
    left: 323px; top: 60px;
    font-weight: 500;
    font-size: 22px;
    letter-spacing: 4px;
    color: var(--orange);
    line-height: 1.1;
  }
  .contact { position: absolute; left: 323px; top: 204px; color: var(--graphite); }
  .contact__name {
    font-weight: 600;
    font-size: 19px;
    letter-spacing: 0.5px;
    margin-bottom: 20px;
  }
  .contact__name .first { color: var(--orange); }
  .contact__line { font-size: 14.5px; line-height: 17px; }
  .contact__web { font-size: 14.5px; margin-top: 15px; }
  .contact__web strong { color: var(--orange); font-weight: 600; }

  .back-brand {
    display: flex;
    align-items: center;
    gap: 18px;
  }
  .back-brand__square {
    width: 22px; height: 22px;
    background: var(--orange);
  }
  .back-brand__name {
    font-weight: 500;
    font-size: 27px;
    letter-spacing: 7px;
    color: var(--white);
    line-height: 1;
  }
</style>
</head>
<body>
  <section class="card card--front">
    <div class="product-photo" role="img" aria-label="Photo from above of a black steel triangular fire pit with burning logs on dark gravel"></div>
    <div class="accent-bar"></div>
    <div class="accent-notch"></div>
    <div class="brand-name">LANTERN<br>HEARTHWORKS</div>
    <div class="contact">
      <p class="contact__name"><span class="first">MILES</span> ARDENT</p>
      <p class="contact__line">503-555-0147</p>
      <p class="contact__line">miles.a@lanternhearthworks.com</p>
      <p class="contact__web">www.<strong>lanternhearthworks</strong>.com</p>
    </div>
  </section>

  <section class="card card--back">
    <div class="back-brand">
      <span class="back-brand__square"></span>
      <span class="back-brand__name">LANTERN HEARTHWORKS</span>
    </div>
  </section>
</body>
</html>
```